Brightwell Power "Unique Process" Graphic

Create a "graphic" that creatively represents the seven-step process that Brightwell Power uses to serve our customers.
This graphic should be sized in such a way that it can easily be included on a page in our website, and also used in other marketing materials such as flyers, emails and powerpoint presentations.
As an EXAMPLE of a similar graphic, see the "Proven Process" section of the home page of this website - https://www.northvanetek.example/
I'll include our brand documentation as well as the document for our "Unique Process" in the uploaded files section.
Please use our brand colors and also be creative in how you represent the seven steps graphically.
Here's a bit about our business.
Brightwell Power is one of the largest B2B Energy Brokers in the US. We serve tens of thousands of customers by securing energy contracts for them. We are NOT an energy company ourselves - but a broker that represents 30+ energy suppliers to commercial and nonprofit customers.

```html
<!DOCTYPE html>
<html lang="en">
<head>
<meta charset="utf-8">
<title>Brightwell Power – Seven-Step Process</title>
<link rel="stylesheet" href="https://fonts.googleapis.com/css2?family=Archivo:ital,wght@0,800;0,900;1,800;1,900&family=Lato:wght@400;700&display=swap">
<style>
  :root {
    --navy: #0f2f6e;
    --navy-deep: #0b2358;
    --green: #0a9a45;
    --green-deep: #05732f;
    --grey: #8c8c8c;
    --grey-light: #b5b5b5;
    --ink: #111111;
    --body: #555555;
    --paper: #ffffff;
  }
  * { margin: 0; padding: 0; box-sizing: border-box; }
  html, body { width: 1200px; height: 675px; overflow: hidden; background: var(--paper); }
  .canvas { position: relative; width: 1200px; height: 675px; overflow: hidden; background: var(--paper); font-family: "Lato", sans-serif; }

  .title { position: absolute; top: 56px; left: 0; width: 100%; text-align: center; font-family: "Archivo", sans-serif; font-weight: 900; font-size: 40px; letter-spacing: -0.5px; line-height: 1; text-shadow: 1px 2px 2px rgba(0,0,0,.25); }
  .title .brand-blue { color: var(--navy); }
  .title .brand-green { color: var(--green); }
  .subtitle { position: absolute; top: 106px; left: 0; width: 100%; text-align: center; font-family: "Archivo", sans-serif; font-weight: 900; font-style: italic; font-size: 29px; color: var(--ink); line-height: 1; text-shadow: 1px 2px 2px rgba(0,0,0,.2); }

  .process-wheel { position: absolute; left: 0; top: 0; }

  .step { position: absolute; }
  .step h2 { font-family: "Archivo", sans-serif; font-weight: 900; font-size: 19.5px; line-height: 1; margin-bottom: 9px; text-shadow: 1px 1px 1px rgba(0,0,0,.22); white-space: nowrap; }
  .step p { font-size: 15px; line-height: 18px; color: var(--body); }
  .step.align-right { text-align: right; }
  .h-grey { color: var(--grey); }
  .h-green { color: var(--green); }
  .h-navy { color: var(--navy); }

  .step-assessment { left: 830px; top: 177px; }
  .step-options { left: 855px; top: 273px; }
  .step-signup { left: 869px; top: 436px; }
  .step-qa { left: 759px; top: 557px; }
  .step-guarantee { right: 768px; top: 200px; }
  .step-renewal { right: 826px; top: 332px; }
  .step-monitoring { right: 765px; top: 527px; }

  .step-number { font-family: "Archivo", sans-serif; font-weight: 900; font-size: 34px; fill: #fff; text-anchor: middle; }
  .center-name { font-family: "Lato", sans-serif; font-weight: 700; font-size: 14px; fill: var(--navy); text-anchor: middle; }
</style>
</head>
<body>
<main class="canvas">
  <h1 class="title"><span class="brand-blue">BRIGHTWELL</span> <span class="brand-green">POWER</span></h1>
  <div class="subtitle">SEVEN-STEP PROCESS</div>

  <svg class="process-wheel" width="1200" height="675" viewBox="0 0 1200 675" aria-label="Seven-step process wheel">
    <defs>
      <linearGradient id="grad-grey" x1="0" y1="0" x2="1" y2="1">
        <stop offset="0" stop-color="#6f6f6f"/><stop offset="1" stop-color="#bdbdbd"/>
      </linearGradient>
      <linearGradient id="grad-green" x1="0" y1="0" x2="1" y2="1">
        <stop offset="0" stop-color="#05732f"/><stop offset="1" stop-color="#0fae4f"/>
      </linearGradient>
      <linearGradient id="grad-navy" x1="0" y1="0" x2="1" y2="1">
        <stop offset="0" stop-color="#0b2358"/><stop offset="1" stop-color="#163d85"/>
      </linearGradient>
      <radialGradient id="grad-hub" cx="0.45" cy="0.4" r="0.7">
        <stop offset="0" stop-color="#ffffff"/><stop offset="1" stop-color="#dcdfe3"/>
      </radialGradient>
      <path id="petal" d="M -30.7 -62.9 C -45 -100 -60 -140 -55 -172 C -40 -200 20 -212 95 -168 C 75 -130 55 -95 30.7 -62.9 A 70 70 0 0 0 -30.7 -62.9 Z"/>
    </defs>

    <!-- leader lines -->
    <g class="leaders" fill="none" stroke="#222" stroke-width="1" stroke-dasharray="3 3">
      <polyline points="810,215 758,215 729,243"/>
      <polyline points="836,314 807,314 792,335"/>
      <polyline points="840,479 808,479 799,468"/>
      <polyline points="737,581 696,581 685,568"/>
      <polyline points="456,576 498,576 519,552"/>
      <polyline points="385,348 422,348 438,370"/>
      <polyline points="447,206 482,206 501,233"/>
    </g>
    <g class="leader-dots" fill="#111">
      <circle cx="810" cy="215" r="3.5"/><circle cx="836" cy="314" r="3.5"/>
      <circle cx="840" cy="479" r="3.5"/><circle cx="737" cy="581" r="3.5"/>
      <circle cx="456" cy="576" r="3.5"/><circle cx="385" cy="348" r="3.5"/>
      <circle cx="447" cy="206" r="3.5"/>
    </g>

    <g transform="translate(624 382)">
      <g class="petals" stroke="#fff" stroke-width="3">
        <use href="#petal" fill="url(#grad-navy)" transform="rotate(333.4)"/>
        <use href="#petal" fill="url(#grad-green)" transform="rotate(282)"/>
        <use href="#petal" fill="url(#grad-grey)" transform="rotate(230.6)"/>
        <use href="#petal" fill="url(#grad-green)" transform="rotate(179.2)"/>
        <use href="#petal" fill="url(#grad-navy)" transform="rotate(127.8)"/>
        <use href="#petal" fill="url(#grad-green)" transform="rotate(76.4)"/>
        <use href="#petal" fill="url(#grad-grey)" transform="rotate(25)"/>
      </g>
      <circle r="100" fill="none" stroke="rgba(255,255,255,.22)" stroke-width="26"/>
      <circle r="72" fill="url(#grad-hub)" stroke="#e9ecef" stroke-width="3"/>
      <text class="center-name" x="0" y="-2">Brightwell</text>
      <text class="center-name" x="0" y="16">Power</text>
    </g>

    <g class="numbers">
      <text class="step-number" x="682" y="268">01</text>
      <text class="step-number" x="737" y="361">02</text>
      <text class="step-number" x="744" y="473">03</text>
      <text class="step-number" x="624" y="520">04</text>
      <text class="step-number" x="530" y="500">05</text>
      <text class="step-number" x="490" y="362">06</text>
      <text class="step-number" x="554" y="295">07</text>
    </g>
  </svg>

  <section class="step step-assessment">
    <h2 class="h-grey">BRIGHTWELL ASSESSMENT</h2>
    <p>Spend 15 minutes with our team<br>while we analyze your account</p>
  </section>
  <section class="step step-options">
    <h2 class="h-green">BRIGHTWELL OPTIONS</h2>
    <p>We’ll send you an energy quote with at least<br>three options to choose from - including<br>different suppliers and contract terms. Our<br>unbiased advice will help you find the</p>
  </section>
  <section class="step step-signup">
    <h2 class="h-navy">BRIGHTWELL SIGN-UP</h2>
    <p>Our simple sign-up process is<br>handled electronically. Even<br>contract<br>signatures.</p>
  </section>
  <section class="step step-qa">
    <h2 class="h-green">BRIGHTWELL QA</h2>
    <p>Every order detail is confirmed to<br>ensure accuracy and smooth<br>processing.</p>
  </section>
  <section class="step step-guarantee align-right">
    <h2 class="h-navy">BRIGHTWELL GUARANTEE</h2>
    <p>Sleep Easy! You’ll never fall “out of<br>contract” with Brightwell as<br>your broker.</p>
  </section>
  <section class="step step-renewal align-right">
    <h2 class="h-green">BRIGHTWELL RENEWAL</h2>
    <p>To protect your business from market<br>volatility, we contact you<br>ahead of your contract end date to discuss<br>renewal options. If anyone else contacts<br>you, you<br>respond, “No thank you, we have<br>Brightwell!”</p>
  </section>
  <section class="step step-monitoring align-right">
    <h2 class="h-grey">BRIGHTWELL MONITORING</h2>
    <p>We proactively monitor your<br>accounts to address any contractual<br>issues with suppliers, should they<br>arise. (E.g., You sell your business,<br>account number changes,<br>.</p>
  </section>
</main>
</body>
</html>
```